The Bean Lantern - Looking for a stylish, cool, hipster style logo and website look and feel.

We need a logo and screen design for an e-commerce website that offers a variety of coffee blends to customers.
We first need a logo, and subsequently a theme for the entire website.
The design can be hipster/rustic/stylish, as it fits in the barrister/coffee culture environment. We are imagining a black/white logo and theme, which can also use an additional accent colour (we are open to suggestions).
In short, what we need: 1. A logo "The Bean Lantern", and a selection of fonts/accent colours for our platform.

Target Market(s)

Our target market is customers who shop coffee online. They are typically between 25 and 50 years old and value a very clean, crisp, stylish, professional design.

Industry/Entity Type

Coffee Shop

Contact Information for Business Card

logo, company name, more details to follow

Logo Text

The Bean Lantern

Number of Pages Required

1 page

Font styles to use
Sans Serif

Colors
474747
333333
000000
ffffff

Requirements
Must have
• Please note that the market we are operating in is very stylish. Some examples of the industry here:
• https://www.quillharbour.com.au/
• http://marcoandfennels.com.au/
• It is essential that our design is stylish and cool.
Nice to have
• We are looking for a very stylish, cool, minimalistic (even hipster) look and feel.
• If more text is needed for a logo, you can add:
• Australia
• Australia's best roasters
• Speciality Coffee
Should not have
• Please no brown colour (as the association with coffee).

```html
<!DOCTYPE html>
<html lang="en">
<head>
<meta charset="utf-8">
<title>The Bean Lantern</title>
<link rel="stylesheet" href="https://fonts.googleapis.com/css2?family=Exo+2:wght@400;500;600&family=Lato:wght@400;700&display=swap">
<style>
:root{
  --ink:#000000;
  --charcoal:#333333;
  --graphite:#474747;
  --paper:#ffffff;
  --mist:#a7a7a7;
  --field:#ececec;
  --line:rgba(255,255,255,.85);
}
*{box-sizing:border-box;margin:0;padding:0}
html,body{width:1200px;height:3435px;overflow:hidden;background:var(--paper)}
body{font-family:"Lato",sans-serif;color:var(--paper);position:relative}

.site-header{position:absolute;top:0;left:0;width:1200px;height:126px;background:var(--paper);color:var(--ink)}
.brand{position:absolute;left:92px;top:30px;display:flex;align-items:center;gap:12px}
.brand-mark{width:16px;height:16px;background:var(--ink)}
.brand-name{font-family:"Exo 2",sans-serif;font-weight:600;font-size:30px;letter-spacing:1px;text-transform:uppercase;color:var(--ink)}
.main-nav{position:absolute;top:52px;left:531px;display:flex;align-items:center;font-family:"Exo 2",sans-serif;font-size:14px;text-transform:uppercase;letter-spacing:.5px}
.main-nav a{color:var(--charcoal);text-decoration:none;margin-right:38px}
.main-nav a.active{border:1.5px solid var(--graphite);border-radius:14px;padding:4px 20px}
.cart{position:absolute;left:1082px;top:52px}

.band{position:absolute;left:0;width:1200px;overflow:hidden}
.band-photo{position:absolute;inset:0}
.band-content{position:absolute;left:0;width:100%;display:flex;flex-direction:column;align-items:center;text-align:center}
.band-title{font-family:"Exo 2",sans-serif;font-weight:500;font-size:50px;letter-spacing:3px;text-transform:uppercase;line-height:1;padding:0 24px 12px;border-bottom:3px solid var(--line)}
.band-text{margin-top:14px;font-size:18px}
.btn-outline{margin-top:26px;display:inline-flex;align-items:center;gap:8px;height:36px;padding:0 18px;border:1.5px solid var(--line);color:var(--paper);font-family:"Exo 2",sans-serif;font-size:13px;text-transform:uppercase;text-decoration:none}
.icon{margin-bottom:10px}

.hero{top:126px;height:561px}
.hero .band-photo{background:radial-gradient(ellipse at 55% 40%,#5a2a2a 0%,#3e4a2a 45%,#23301c 100%)}
.hero .band-content{top:180px}
.hero .band-title{font-size:36px;letter-spacing:1px;border:none;padding:0;border-top:3px solid var(--line);padding-top:18px;width:470px}

.location{top:687px;height:504px}
.location .band-photo{background:linear-gradient(180deg,#4d4438 0%,#3a342c 50%,#2e2a25 100%)}
.wholesale{top:1191px;height:508px}
.wholesale .band-photo{background:radial-gradient(ellipse at 40% 40%,#3a3634 0%,#211e1d 60%,#121111 100%)}
.explore{top:1699px;height:511px}
.explore .band-photo{background:radial-gradient(ellipse at 65% 30%,#6a2b2b 0%,#3c4d33 45%,#27371f 100%)}
.shop{top:2210px;height:510px}
.shop .band-photo{background:linear-gradient(180deg,#2b2722 0%,#3f342a 55%,#2a241f 100%)}
.feature .band-content{top:140px}

.newsletter{position:absolute;top:2720px;left:0;width:1200px;height:362px;background:var(--mist);text-align:center}
.newsletter h2{position:absolute;top:40px;left:0;width:100%;font-family:"Exo 2",sans-serif;font-weight:400;font-size:42px;letter-spacing:2px}
.newsletter .rule{position:absolute;top:100px;left:450px;width:300px;height:2px;background:var(--paper)}
.newsletter p{position:absolute;top:135px;left:0;width:100%;font-size:18px}
.field{position:absolute;top:193px;height:40px;width:460px;background:var(--field);border:1px solid #cfcfcf;color:var(--graphite);font-size:13px;text-align:left;padding:12px 14px}
.btn-solid{position:absolute;top:265px;left:504px;width:190px;height:44px;background:var(--charcoal);color:var(--paper);font-family:"Exo 2",sans-serif;font-weight:600;font-size:16px;text-transform:uppercase;display:flex;align-items:center;justify-content:center;gap:8px}

.site-footer{position:absolute;top:3082px;left:0;width:1200px;height:353px;background:var(--ink)}
.col{position:absolute;top:36px}
.col h3{font-family:"Exo 2",sans-serif;font-weight:500;font-size:16px;text-transform:uppercase;padding-bottom:14px;border-bottom:1px solid #3a3a3a}
.links{list-style:none;margin-top:16px;font-size:12px}
.links li{height:38px;display:flex;align-items:center}
.links li::before{content:"";width:5px;height:5px;border-radius:50%;background:var(--paper);margin-right:12px}
.contact-row{display:flex;gap:14px;font-size:12px;margin-top:22px;line-height:1.4}
.inquiry-field{width:263px;height:24px;border:1px solid #bdbdbd;font-size:11px;padding:4px 8px;margin-top:9px}
.inquiry-submit{margin-top:10px;width:96px;height:28px;background:var(--graphite);font-family:"Exo 2",sans-serif;font-weight:600;font-size:15px;text-transform:uppercase;display:flex;align-items:center;justify-content:center}
.social{list-style:none;margin-top:14px;font-size:12px}
.social li{height:41px;display:flex;align-items:center;gap:14px}
.social li::before{content:"";width:32px;height:32px;border-radius:50%;border:1.5px solid var(--paper)}
.footer-rule{position:absolute;top:296px;left:92px;width:1016px;height:1px;background:#3a3a3a}
.copyright{position:absolute;top:318px;left:0;width:100%;text-align:center;font-size:12px}
</style>
</head>
<body>

<header class="site-header">
  <div class="brand"><span class="brand-mark"></span><span class="brand-name">The Bean Lantern</span></div>
  <nav class="main-nav">
    <a class="active" href="#">Coffee</a><a href="#">Locations</a><a href="#">Wholesale</a><a href="#">Explore</a><a href="#">Shop</a>
  </nav>
  <svg class="cart" width="24" height="22" viewBox="0 0 24 22" fill="none" stroke="#333" stroke-width="2"><path d="M1 2h4l3 12h12l3-9H7"/><circle cx="10" cy="19" r="1.8"/><circle cx="19" cy="19" r="1.8"/></svg>
</header>

<section class="band hero">
  <div class="band-photo" role="img" aria-label="Close-up of ripe red coffee cherries on the branch"></div>
  <div class="band-content">
    <svg class="icon" width="44" height="36" viewBox="0 0 44 36" fill="#fff"><path d="M6 14h26v10a10 10 0 0 1-10 10h-6A10 10 0 0 1 6 24z"/><path d="M32 16h4a5 5 0 0 1 0 10h-4v-3h4a2 2 0 0 0 0-4h-4z"/><path d="M16 2c-3 4 3 5 0 10M22 2c-3 4 3 5 0 10" stroke="#fff" stroke-width="2" fill="none"/></svg>
    <h1 class="band-title">Australia's Best Roasters Coffee</h1>
    <a class="btn-outline" href="#">Find out more <span>&#9656;</span></a>
  </div>
</section>

<section class="band feature location">
  <div class="band-photo" role="img" aria-label="Café counter with baristas under pendant lights"></div>
  <div class="band-content">
    <svg class="icon" width="30" height="44" viewBox="0 0 30 44"><path d="M15 1a14 14 0 0 0-14 14c0 11 14 28 14 28s14-17 14-28A14 14 0 0 0 15 1z" fill="#fff"/><circle cx="15" cy="15" r="5" fill="#3a342c"/></svg>
    <h2 class="band-title">Location</h2>
    <p class="band-text">Lorem autem vel eum iriure hendrerit in vulputate velit esse molestie.</p>
    <a class="btn-outline" href="#">Find out more <span>&#9656;</span></a>
  </div>
</section>

<section class="band feature wholesale">
  <div class="band-photo" role="img" aria-label="Espresso machine pouring into cups"></div>
  <div class="band-content">
    <svg class="icon" width="38" height="44" viewBox="0 0 38 44" fill="none" stroke="#fff" stroke-width="3"><rect x="3" y="14" width="32" height="28"/><path d="M12 18V9a7 7 0 0 1 14 0v9"/></svg>
    <h2 class="band-title">Wholesale</h2>
    <p class="band-text">Lorem autem vel eum iriure hendrerit in vulputate velit esse molestie.</p>
    <a class="btn-outline" href="#">Find out more <span>&#9656;</span></a>
  </div>
</section>

<section class="band feature explore">
  <div class="band-photo" role="img" aria-label="Coffee plant leaves with clusters of red cherries"></div>
  <div class="band-content">
    <svg class="icon" width="44" height="44" viewBox="0 0 44 44"><circle cx="22" cy="22" r="19" fill="none" stroke="#fff" stroke-width="3"/><path d="M31 13l-6 13-12 5 6-13z" fill="#fff"/></svg>
    <h2 class="band-title">Explore</h2>
    <p class="band-text">Lorem autem vel eum iriure hendrerit in vulputate velit esse molestie.</p>
    <a class="btn-outline" href="#">Find out more <span>&#9656;</span></a>
  </div>
</section>

<section class="band feature shop">
  <div class="band-photo" role="img" aria-label="Empty café interior with tables and hanging lamps"></div>
  <div class="band-content">
    <svg class="icon" width="44" height="42" viewBox="0 0 44 42"><path d="M4 16h36l-5 24H9z" fill="#fff"/><path d="M12 16a10 10 0 0 1 20 0" fill="none" stroke="#fff" stroke-width="3"/></svg>
    <h2 class="band-title">Shop</h2>
    <p class="band-text">Lorem autem vel eum iriure hendrerit in vulputate velit esse molestie.</p>
    <a class="btn-outline" href="#">Find out more <span>&#9656;</span></a>
  </div>
</section>

<section class="newsletter">
  <h2>NEWSLETTER SIGNUP</h2>
  <div class="rule"></div>
  <p>Lorem autem vel eum iriure hendrerit in vulputate velit esse molestie.</p>
  <div class="field" style="left:121px">Enter your name</div>
  <div class="field" style="left:618px">Enter your email</div>
  <div class="btn-solid">Subscribe now! <span>&#9656;</span></div>
</section>

<footer class="site-footer">
  <div class="col" style="left:92px;width:120px">
    <h3>Quick Links</h3>
    <ul class="links"><li>Coffee</li><li>Locations</li><li>Wholesale</li><li>Explore</li><li>Shop</li></ul>
  </div>
  <div class="col" style="left:289px;width:270px">
    <h3>Contact Details</h3>
    <div class="contact-row"><svg width="12" height="16" viewBox="0 0 12 16"><path d="M6 0a6 6 0 0 0-6 6c0 4 6 10 6 10s6-6 6-10a6 6 0 0 0-6-6z" fill="#fff"/></svg><span>Lorem autem vel eum iriure hendrerit in<br>vulputate velit esse - 012345</span></div>
    <div class="contact-row"><svg width="14" height="14" viewBox="0 0 14 14"><path d="M3 0l3 3-2 2a8 8 0 0 0 5 5l2-2 3 3-2 3C6 14 0 8 0 3z" fill="#fff"/></svg><span>012-345-6789</span></div>
    <div class="contact-row"><svg width="14" height="14" viewBox="0 0 14 14"><rect x="1" y="4" width="12" height="8" fill="#fff"/><rect x="3" y="0" width="8" height="5" fill="none" stroke="#fff"/></svg><span>012-345-6789</span></div>
    <div class="contact-row"><svg width="14" height="12" viewBox="0 0 14 12"><rect x="0" y="1" width="14" height="10" fill="#fff"/><path d="M0 1l7 6 7-6" stroke="#000" fill="none"/></svg><span>info@thebeanlantern.com</span></div>
  </div>
  <div class="col" style="left:637px;width:263px">
    <h3>Quick Inquiry</h3>
    <div class="inquiry-field">Your Name</div>
    <div class="inquiry-field">Phone</div>
    <div class="inquiry-field">Email</div>
    <div class="inquiry-field">Your Name</div>
    <div class="inquiry-submit">Submit</div>
  </div>
  <div class="col" style="left:980px;width:128px">
    <h3>Follow Us</h3>
    <ul class="social"><li>Friendcast</li><li>Chirpline</li><li>Worklink</li><li>Searchplus</li></ul>
  </div>
  <div class="footer-rule"></div>
  <p class="copyright">Copyright © 2017 The Bean Lantern. All Rights Reserved.</p>
</footer>

</body>
</html>
```